Business Card Design for Translation Company - Rush

Rush job for a business card designing for a company doing international translations, several Asian and western languages. Already have a logo design (see attached) to use as the basis of the business card design. For the card, we also need the full company name, address, email, and phone number. In addition, my name as I will be the one handing out the cards.

For the logo design, we think the white background would be best. But we will consider using the dark background if you have a great idea for it.

The attached jpeg design has just been approved, but the designer has not yet finalized the file. When we select our final applicant, we will send the finalized file. (Nothing changes except the quality of the data.)

The phone number may change and if so, we will send the new one when we select our applicant.

We must complete the entire process and have a design ready to go to print no later than 01:00 am August 3, New York (East Coast) time.

We look forward to your participation in the project,
Gus

Target Market(s)

Translation clients worldwide.

Industry/Entity Type

Business

Contact Information for Business Card

Company details:

Korvani Languages Worldwide, Ltd.

#527-2368 Halden Crescent, Victoria, BC, Canada V9T3K2

gdresner@korvanilanguages.example

+1-888-604-2731

Font styles to use
Sans Serif

Requirements
Must have
• Company name, address, email and phone number.
• Also my name:
• Gustav R. Dresner
• Director
Nice to have
• Not a demand, but please consider creatively using the horizontal bar.
Should not have
• Cluttered of jumbled appearance.

```html
<!DOCTYPE html>
<html lang="en">
<head>
<meta charset="utf-8">
<title>Korvani Languages – Business Card</title>
<link rel="stylesheet" href="https://fonts.googleapis.com/css2?family=Arimo:wght@400;700&display=swap">
<style>
  :root {
    --canvas: #ecebe8;
    --charcoal: #333436;
    --slate: #3c3d40;
    --orange: #e07a2e;
    --paper: #f4f4f4;
    --ink: #2e2e2e;
    --grey-text: #a9a9a9;
  }
  * { box-sizing: border-box; margin: 0; padding: 0; }
  html, body { width: 1200px; height: 800px; overflow: hidden; }
  body {
    background: var(--canvas);
    font-family: "Arimo", Arial, sans-serif;
    position: relative;
  }
  .card {
    position: absolute;
    top: 257px;
    width: 500px;
    height: 286px;
    overflow: hidden;
    box-shadow: 0 10px 24px rgba(0,0,0,0.18);
  }
  /* Front: dark brand side */
  .card--front { left: 60px; background: var(--charcoal); }
  .brand {
    position: absolute;
    left: 70px;
    top: 120px;
    display: flex;
    align-items: center;
    gap: 16px;
  }
  .brand__dot {
    width: 34px; height: 34px;
    border-radius: 50%;
    background: var(--orange);
  }
  .brand__name {
    color: var(--grey-text);
    font-size: 22px;
    font-weight: 400;
    letter-spacing: 0.22em;
    text-transform: uppercase;
  }
  .brand__bar {
    position: absolute;
    left: 120px;
    top: 168px;
    width: 300px;
    height: 2px;
    background: var(--orange);
  }
  /* Back: white contact side */
  .card--back { left: 640px; background: var(--paper); }
  .card__graphic { position: absolute; left: 0; top: 0; }
  .contact {
    position: absolute;
    left: 230px;
    top: 40px;
    color: var(--ink);
    font-size: 12.5px;
    line-height: 1.35;
  }
  .contact__name { font-size: 17px; font-weight: 700; }
  .contact__role { font-size: 16px; font-weight: 700; color: var(--orange); margin-bottom: 22px; }
  .contact__company { font-weight: 700; }
  .contact__address { margin-bottom: 18px; }
  .contact__line { display: flex; align-items: center; gap: 6px; margin-top: 3px; }
  .contact__icon { width: 15px; height: 15px; flex: none; }
</style>
</head>
<body>
  <section class="card card--front" aria-label="Card front">
    <div class="brand">
      <span class="brand__dot"></span>
      <span class="brand__name">Korvani Languages</span>
    </div>
    <div class="brand__bar"></div>
  </section>

  <section class="card card--back" aria-label="Card back">
    <svg class="card__graphic" width="500" height="286" viewBox="0 0 500 286" aria-hidden="true">
      <path d="M0 0 H70 C40 90 40 190 70 286 H0 Z" fill="var(--slate)"/>
      <path d="M80 0 H190 C150 90 150 190 190 286 H80 C50 190 50 90 80 0 Z" fill="var(--orange)"/>
    </svg>
    <div class="contact">
      <p class="contact__name">Gustav R. Dresner</p>
      <p class="contact__role">Director</p>
      <p class="contact__company">Korvani Languages Worldwide, Ltd.</p>
      <p class="contact__address">#527-2368 Halden Crescent,<br>Victoria, BC, Canada<br>V9T3K2</p>
      <p class="contact__line">
        <svg class="contact__icon" viewBox="0 0 16 16" aria-hidden="true"><circle cx="8" cy="8" r="8" fill="var(--orange)"/><rect x="5" y="3.5" width="6" height="9" rx="1" fill="none" stroke="#fff" stroke-width="1.3"/></svg>
        +1-888-604-2731
      </p>
      <p class="contact__line">
        <svg class="contact__icon" viewBox="0 0 16 16" aria-hidden="true"><circle cx="8" cy="8" r="8" fill="var(--orange)"/><rect x="4" y="5" width="8" height="6" fill="none" stroke="#fff" stroke-width="1.2"/><path d="M4 5 L8 8.5 L12 5" fill="none" stroke="#fff" stroke-width="1.2"/></svg>
        gdresner@korvanilanguages.example
      </p>
    </div>
  </section>
</body>
</html>
```